Postcard Design

I need a postcard to use as a mailer and handout piece to get a new vacation rental management company off the ground. This will be sent to rental property owners in Merindel on 30a in Florida.

A google image search of "Merindel 30A" will provide plenty of images for look and feel of the project. A quick google of "coastal modern design" will provide some feel for interiors and a color palette using the beachy but subtle colors typical to that decor.

Merindel is a 130 unit condominium complex in a very active beach rental market. The tone of the community is upscale family vacations...it is NOT a party destination. Beach and family time are what most people are here for.

Logo file uploaded here.

If good design comes in quickly I may zero in on one quickly to tweak it and get things moving.

Target audience is property owners who we hope to bring in as rental owners. The audience is not rental guests. Try to sell to property owners who you want to trust us with their investments.

We offer a full lineup of services including top-notch housekeeping, maintenance, marketing, and guest services.

We want to build relationships with our property owners.

We are a small team focused on only Merindel properties.

Designers...please feel free to suggest any wording or tag lines that you think sell this idea. Your creativity with the copy is as valuable as your visual creativity.

Some copy scraps & messaging to play with:

Tailored exclusively to Merindel and its owners

Boutique Rental Management

Full service maintenance and housekeeping

Merindel's reputation is our reputation

Thank you all.

I just updated he brief to provide some added guidance. Thanks!

Boutique

```html
<!DOCTYPE html>
<html lang="en">
<head>
<meta charset="utf-8">
<title>Merindel Postcard – Front and Back</title>
<link rel="stylesheet" href="https://fonts.googleapis.com/css2?family=Arimo:wght@400&family=Tinos:wght@400&display=swap">
<style>
  :root {
    --page-bg: #ffffff;
    --band-brown: #7b6560;
    --panel-sage: #d3dbd3;
    --body-text: #4b4b4b;
    --logo-brown: #3e2b26;
    --back-cream: #faf2e5;
    --back-border: #5a5a5a;
    --rule-brown: #5d4a44;
    --stamp-tan: #dccbab;
    --stamp-frame: #f4ead8;
    --photo-pool-a: #8fb7c9;
    --photo-pool-b: #6f9a6a;
    --photo-building-a: #6f97d6;
    --photo-building-b: #d8c98e;
    --photo-boardwalk-a: #5d9ad8;
    --photo-boardwalk-b: #8d8276;
  }
  * { margin: 0; padding: 0; box-sizing: border-box; }
  html, body {
    width: 1200px; height: 1000px; overflow: hidden;
    background: var(--page-bg);
  }
  .canvas { position: relative; width: 1200px; height: 1000px; }

  /* Front */
  .postcard-front {
    position: absolute; left: 50px; top: 295px;
    width: 528px; height: 409px;
    background: var(--panel-sage);
    overflow: hidden;
  }
  .photo-strip { position: absolute; left: 0; top: 0; width: 528px; height: 167px; }
  .photo { position: absolute; top: 0; height: 167px; }
  .photo-pool { left: 0; width: 132px;
    background: linear-gradient(180deg, var(--photo-pool-b) 0%, #a7c6cf 45%, var(--photo-pool-a) 100%); }
  .photo-building { left: 132px; width: 266px;
    background: linear-gradient(180deg, var(--photo-building-a) 0%, var(--photo-building-b) 40%, #c7b57a 75%, #8a9a6a 100%); }
  .photo-boardwalk { left: 398px; width: 130px;
    background: linear-gradient(180deg, var(--photo-boardwalk-a) 0%, #9cc4e2 40%, #b7b3a6 60%, var(--photo-boardwalk-b) 100%); }

  .headline-band {
    position: absolute; left: 0; top: 167px; width: 528px; height: 48px;
    background: var(--band-brown);
    box-shadow: 0 3px 4px rgba(0,0,0,0.18);
    display: flex; align-items: center; justify-content: center;
  }
  .headline {
    font-family: "Tinos", Georgia, serif; font-weight: 400;
    font-size: 25px; color: #ffffff; letter-spacing: 0.1px;
  }
  .pitch {
    position: absolute; left: 31px; top: 229px; width: 300px;
    font-family: "Arimo", Arial, sans-serif; font-size: 12.6px;
    line-height: 16.5px; color: var(--body-text);
  }
  .pitch p { margin-bottom: 8px; }
  .pitch .wide { width: 310px; }

  .front-signoff {
    position: absolute; left: 345px; top: 316px; width: 170px;
    text-align: center;
  }
  .brand-name {
    font-family: "Tinos", Georgia, serif; font-weight: 400;
    color: var(--logo-brown);
  }
  .front-signoff .brand-name { font-size: 36px; line-height: 40px; }
  .contact {
    margin-top: 10px;
    font-family: "Arimo", Arial, sans-serif; font-size: 12.3px;
    line-height: 16px; color: var(--body-text);
  }

  /* Back */
  .postcard-back {
    position: absolute; left: 620px; top: 295px;
    width: 530px; height: 409px;
    background: var(--back-cream);
    border: 1px solid var(--back-border);
  }
  .postcard-back .brand-name {
    position: absolute; left: 30px; top: 140px;
    font-size: 48px; line-height: 52px;
  }
  .postcard-back svg { position: absolute; left: 0; top: 0; }
</style>
</head>
<body>
<main class="canvas">

  <section class="postcard-front" aria-label="Postcard front">
    <div class="photo-strip">
      <div class="photo photo-pool" role="img" aria-label="Photo of the resort pool and hot tub with palm trees"></div>
      <div class="photo photo-building" role="img" aria-label="Photo of the Merindel condominium building under blue sky"></div>
      <div class="photo photo-boardwalk" role="img" aria-label="Photo of the wooden boardwalk leading to the beach"></div>
    </div>

    <div class="headline-band">
      <h1 class="headline">Are you looking for a rental opportunity?</h1>
    </div>

    <div class="pitch">
      <p>We know how to manage your properties,<br>we only focus on Merindel's Condo.</p>
      <p>Find your investment opportunity here<br>at the beautiful Merindel by Harborline.</p>
      <p class="wide">Let our real estate professionals personally assist you.</p>
      <p class="wide">We offer state of the art marketing, complete guest services, top notch housekeeping and all year round maintenance.</p>
    </div>

    <div class="front-signoff">
      <div class="brand-name">Merindel</div>
      <div class="contact">Contact us at: Toll Free:<br>(866) 555-0147</div>
    </div>
  </section>

  <section class="postcard-back" aria-label="Postcard back">
    <div class="brand-name">Merindel</div>
    <svg width="530" height="409" viewBox="0 0 530 409" aria-hidden="false">
      <line class="divider" x1="256" y1="25" x2="256" y2="335" stroke="var(--rule-brown)" stroke-width="1"/>
      <g class="stamp-box">
        <rect x="414" y="25" width="84" height="97" fill="var(--stamp-tan)"/>
        <rect x="422" y="33" width="68" height="81" fill="none" stroke="var(--stamp-frame)" stroke-width="1.5"/>
        <rect x="440" y="55" width="32" height="36" rx="4" fill="#e9dcc2" role="img" aria-label="Starfish illustration"/>
      </g>
      <g class="address-lines" stroke="var(--rule-brown)" stroke-width="1">
        <line x1="301" y1="187" x2="498" y2="187"/>
        <line x1="301" y1="225" x2="498" y2="225"/>
        <line x1="301" y1="262" x2="498" y2="262"/>
        <line x1="301" y1="299" x2="498" y2="299"/>
        <line x1="301" y1="337" x2="498" y2="337"/>
      </g>
    </svg>
  </section>

</main>
</body>
</html>
```